Powerpoint and Word Document Template

Our target market are C-suite executives in banks, credit unions, non-bank financial institutions, financial technology companies and in the law firms, private equity firms and the like that are also advising the industry.

design should convey: confidence, trust, expertise, experience, value, advice, relationship focus.

For the stationery design, we will need the .doc format as well.

Industry/Entity Type

Consulting

Font styles to use
Sans Serif

Colors
0356a4
3277b5
85acd3
cedeed
eaf1f7
ffffff

Requirements
Must have
• must use the logo and color scheme included in the attached zip file. must include a powerpoint template with a cover slide, section break slides, slides for images/graphics, slides for side by side content, and slides for regular content.

Note: this should also include designs for word documents like stationary and envelopes based on the same concept.

```html
<!DOCTYPE html>
<html lang="en">
<head>
<meta charset="utf-8">
<title>Vantrel Advisory – Presentation Template</title>
<link href="https://fonts.googleapis.com/css2?family=Rubik:wght@300;400;500;700&display=swap" rel="stylesheet">
<style>
:root{
  --navy:#0b3a7c;
  --brand:#0356a4;
  --mid:#3277b5;
  --soft:#85acd3;
  --pale:#cedeed;
  --mist:#eaf1f7;
  --white:#ffffff;
  --grey:#58595b;
  --grey-dark:#3f4042;
  --grey-box:#6d6e71;
  --text:#5a5a5a;
  --frame:#e2e2e2;
}
*{box-sizing:border-box;margin:0;padding:0}
html,body{width:1200px;height:2265px;overflow:hidden}
body{background:var(--frame);font-family:'Rubik',sans-serif;color:var(--text);position:relative}

.site-header{position:absolute;left:0;top:0;width:1200px;height:145px;background:var(--white);display:flex;align-items:center;justify-content:center;gap:14px}
.brand-square{width:40px;height:40px;background:var(--brand)}
.brand-name{font-weight:500;color:var(--brand);font-size:34px;letter-spacing:3px}

.hero{position:absolute;left:4px;top:145px;width:1192px;height:516px;background:linear-gradient(155deg,#2b5a93 0%,#1f4d89 35%,#174481 65%,#23528d 100%);color:var(--white);text-align:center}
.hero-title{position:absolute;left:0;right:0;top:196px;font-size:48px;font-weight:500;letter-spacing:-0.5px}
.hero-sub{position:absolute;left:0;right:0;top:250px;font-size:16px;letter-spacing:11px;font-weight:300}
.hero-by{position:absolute;left:0;right:0;top:376px;font-size:14px;letter-spacing:9px;font-weight:300}
.hero-name{position:absolute;left:0;right:0;top:396px;font-size:16px;font-weight:700;letter-spacing:1.5px}
.hero-social{position:absolute;left:0;right:0;top:466px;display:flex;justify-content:center;gap:5px}
.hero-social span{width:30px;height:30px;border:2px solid var(--white);border-radius:50%}

.deck{position:absolute;left:4px;top:679px;display:grid;grid-template-columns:repeat(3,393px);grid-auto-rows:222px;gap:5px}
.slide{position:relative;background:var(--white);overflow:hidden}
.abs{position:absolute}
.photo{position:absolute}
.tiny{font-size:4.4px;line-height:1.5;color:var(--text)}
.tiny-w{font-size:4.4px;line-height:1.5;color:#dfe8f3}
.pname{font-size:5.6px;font-weight:500;color:var(--brand)}
.s-title{position:absolute;left:0;right:0;top:12px;text-align:center;font-size:14px;color:var(--navy);font-weight:400}
.s-sub{position:absolute;left:0;right:0;top:28px;text-align:center;font-size:5px;color:var(--grey);letter-spacing:.3px}
.s-rule{position:absolute;left:0;right:0;top:36px;height:1px;background:linear-gradient(var(--mist),transparent);box-shadow:0 2px 4px rgba(0,0,0,.05)}

.foot-copy{position:absolute;left:20px;bottom:8px;font-size:3.6px;color:#9a9a9a}
.foot-dash{position:absolute;left:185px;bottom:1px;width:23px;height:2px;background:var(--brand)}
.foot-mark{position:absolute;right:14px;bottom:6px;display:flex;align-items:center;gap:2px;font-size:6px;font-weight:500;color:var(--brand)}
.foot-mark i{width:6px;height:6px;background:var(--brand)}
.foot-mark.light{color:var(--white)}
.foot-mark.light i{background:var(--white)}

.icon-box{position:absolute;width:24px;height:24px;border-radius:5px;background:var(--navy);display:flex;align-items:center;justify-content:center;box-shadow:0 2px 4px rgba(0,0,0,.2)}
.icon-box.lg{width:40px;height:40px;border-radius:7px}
.icon-box svg{width:60%;height:60%}

.mark{display:flex;align-items:center;gap:4px;font-weight:500;color:var(--white)}
.mark i{background:var(--white);display:block}

.agenda-row{position:absolute;left:133px;width:198px;height:15px;border-bottom:1px solid #d9d9d9;display:flex;align-items:center;font-size:6px}
.agenda-row b{width:36px;font-weight:500;color:var(--navy);padding-left:10px}
.card{position:absolute;border-radius:3px;text-align:center;padding:4px}
.num-box{position:absolute;width:18px;height:18px;background:var(--navy);color:var(--white);font-size:6px;font-weight:500;border-radius:3px;display:flex;align-items:center;justify-content:center}
.tbl{position:absolute;left:38px;top:64px;width:328px;display:grid;grid-template-columns:repeat(4,82px);font-size:5px}
.tbl div{padding:4px 6px;height:44px}
.tbl .h{height:20px;background:var(--navy);color:var(--white);font-weight:700;display:flex;align-items:center}
.tbl .c{background:#eef1f4;border-bottom:1px solid var(--white)}
.tbl .hl{background:var(--navy);color:#dfe8f3;border-bottom:1px solid #1f4f8e}
.tbl .hl .pname{color:var(--white)}
.pill{position:absolute;left:55px;width:104px;height:20px;border-radius:5px;background:var(--white);box-shadow:0 1px 5px rgba(0,0,0,.15);display:flex;align-items:center;gap:10px;padding-left:9px;font-size:4.6px;color:var(--grey)}
.pill.on{background:var(--brand);color:var(--white)}
.pill svg{width:8px;height:8px}
.year{position:absolute;width:60px;height:8px;border-radius:4px;background:var(--navy);color:var(--white);font-size:5px;font-weight:500;padding-left:6px;line-height:8px}
.year-dot{position:absolute;width:6px;height:6px;border-radius:50%;background:var(--brand)}
</style>
</head>
<body>

<header class="site-header">
  <span class="brand-square"></span>
  <span class="brand-name">VANTREL ADVISORY</span>
</header>

<section class="hero">
  <div class="photo" style="inset:0;background:linear-gradient(160deg,rgba(255,255,255,.08),rgba(0,0,0,.05) 50%,rgba(255,255,255,.06))" role="img" aria-label="Glass office tower seen from below, blue toned"></div>
  <h1 class="hero-title">PRESENTATION TITLE GOES HERE</h1>
  <p class="hero-sub">SUB TITLE GOES HERE</p>
  <p class="hero-by">PRESENTED BY</p>
  <p class="hero-name">Presenter name</p>
  <div class="hero-social"><span></span><span></span><span></span></div>
</section>

<main class="deck">

  <!-- cover -->
  <article class="slide" style="background:var(--navy)">
    <div class="photo" style="inset:0;background:linear-gradient(120deg,#8e99a8,#4e6787 45%,#223f6d)" role="img" aria-label="Office tower facade, blue toned"></div>
    <div class="abs" style="left:15px;top:15px;width:192px;height:207px;background:var(--navy)"></div>
    <div class="abs mark" style="left:236px;top:60px;font-size:12px"><i style="width:12px;height:12px"></i>VANTREL</div>
    <div class="abs" style="left:236px;top:100px;font-size:13.5px;color:var(--white);line-height:1.3">PRESENTATION<br>TITLE GOES HERE</div>
    <div class="abs" style="left:236px;top:136px;font-size:4.5px;color:var(--white);letter-spacing:3px">SUB TITLE GOES HERE</div>
  </article>

  <!-- page divider -->
  <article class="slide">
    <div class="photo" style="inset:0;background:linear-gradient(135deg,#4a4a4a,#2e2e2e 55%,#3c3c3c)" role="img" aria-label="Laptops on a dark desk, seen from above"></div>
    <div class="abs mark" style="left:30px;top:80px;font-size:12px"><i style="width:12px;height:12px"></i>VANTREL</div>
    <div class="abs" style="left:29px;top:110px;font-size:12.5px;color:var(--white)">HERE ADD YOUR TEXT FOR PAGE DIVIDER</div>
    <p class="abs tiny-w" style="left:29px;top:128px;width:290px">Lorem ipsum dolor sit amet, consectetur adipiscing elit, sed do eiusmod tempor incididunt ut labore et dolore magna aliqua. Ut enim ad minim veniam, quis nostrud exercitation ullamco laboris nisi ut aliquip ex ea commodo.</p>
  </article>

  <!-- slide break -->
  <article class="slide" style="background:var(--navy)">
    <div class="abs" style="left:16px;top:40px;font-size:48px;color:rgba(255,255,255,.12);font-weight:500">01</div>
    <div class="abs" style="left:43px;top:78px;font-size:30px;color:var(--white);line-height:1.05">Slide<br>Break</div>
    <p class="abs tiny-w" style="left:42px;top:144px;width:155px">Lorem ipsum dolor sit amet, consectetur adipiscing elit, sed do eiusmod tempor incididunt ut labore et dolore magna aliqua. Lorem ipsum dolor sit amet, consectetur adipiscing elit, sed do eiusmod tempor incididunt ut labore et dolore magna aliqua. Ut enim ad minim veniam, quis nostrud exercitation ullamco laboris nisi.</p>
  </article>

  <!-- agenda -->
  <article class="slide">
    <div class="photo" style="left:0;top:0;width:158px;height:222px;background:linear-gradient(170deg,#2d5b95,#184681 60%,#244f84)" role="img" aria-label="Business team on a rooftop, blue toned"></div>
    <div class="abs" style="left:33px;top:98px;font-size:21px;color:var(--white)">Agenda</div>
    <div class="agenda-row" style="top:54px"><b>01</b>Introduction - Welcome</div>
    <div class="agenda-row" style="top:69px"><b>02</b>Mission &amp; Vision</div>
    <div class="agenda-row" style="top:84px"><b>03</b>Our Services</div>
    <div class="agenda-row" style="top:100px"><b>04</b>Company Profile</div>
    <div class="agenda-row" style="top:115px"><b>05</b>Company Profile</div>
    <div class="agenda-row" style="top:130px"><b>06</b>Our Team</div>
    <div class="agenda-row" style="top:146px"><b>07</b>Our Offices</div>
    <div class="agenda-row" style="top:161px;border:none"><b>08</b>Q&amp;As / Closing Speech</div>
    <span class="foot-dash"></span>
    <span class="foot-mark"><i></i>VANTREL</span>
  </article>

  <!-- heading text image -->
  <article class="slide">
    <div class="photo" style="left:0;top:0;width:288px;height:168px;background:linear-gradient(120deg,#b6a790,#8b7a66 50%,#c7bba9)" role="img" aria-label="Colleagues shaking hands in a bright office"></div>
    <div class="abs" style="left:220px;top:35px;width:105px;height:95px;border-radius:6px;background:var(--navy);padding:8px 12px;box-shadow:0 3px 8px rgba(0,0,0,.25)">
      <div style="font-size:22px;color:rgba(255,255,255,.2);line-height:.8;font-weight:500">01</div>
      <div style="font-size:6.5px;color:var(--white);font-weight:500;margin-top:-6px">Your Text Here</div>
      <p class="tiny-w" style="margin-top:12px">Lorem ipsum dolor sit amet, consectetur adipiscing elit, sed do eiusmod tempor incididunt ut labore et dolore magna aliqua.</p>
    </div>
    <div class="abs" style="left:32px;top:173px;font-size:21px;color:var(--brand)">Heading + Text + Image Slide</div>
    <span class="foot-copy">COPYRIGHT © (ALL RIGHTS RESERVED)</span>
    <span class="foot-dash"></span>
    <span class="foot-mark"><i></i>VANTREL</span>
  </article>

  <!-- title or quote -->
  <article class="slide">
    <div class="photo" style="left:0;top:0;width:393px;height:96px;background:linear-gradient(100deg,#0e3d7d,#1b4a87 60%,#3a639a)" role="img" aria-label="Office towers, blue toned"></div>
    <div class="abs" style="left:38px;top:28px;font-size:4.6px;letter-spacing:2px;color:var(--white)">SUB TITLE GOES HERE</div>
    <div class="abs" style="left:38px;top:36px;font-size:13.5px;color:var(--white);line-height:1.05">Add Awesome Title Here<br>Or A Quote</div>
    <p class="abs tiny" style="left:34px;top:118px;width:146px;text-align:justify;line-height:2">Lorem ipsum dolor sit amet, consectetur adipiscing elit. Fusce sit amet neque sodales, faucibus ex eu, efficitur lacus. Cras imperdiet, nulla nec sagittis pulvinar, neque augue iaculis risus, ac fringilla felis urna fermentum mi. Ut vehicula vel enim sit amet vulputate. Aenean malesuada consectetur diam, ac convallis quam tincidunt eget. Nam vitae elementum ipsum. Proin vitae blandit enim.</p>
    <p class="abs tiny" style="left:215px;top:118px;width:146px;text-align:justify;line-height:2">Lorem ipsum dolor sit amet, consectetur adipiscing elit. Fusce sit amet neque sodales, faucibus ex eu, efficitur lacus. Cras imperdiet, nulla nec sagittis pulvinar, neque augue iaculis risus, ac fringilla felis urna fermentum mi. Ut vehicula vel enim sit amet vulputate. Aenean malesuada consectetur diam, ac convallis quam tincidunt eget. Nam vitae elementum ipsum. Proin vitae blandit enim.</p>
    <span class="foot-copy">COPYRIGHT © (ALL RIGHTS RESERVED)</span>
    <span class="foot-dash"></span>
    <span class="foot-mark"><i></i>VANTREL</span>
  </article>

  <!-- awesome text with cards -->
  <article class="slide">
    <div class="photo" style="left:0;top:0;width:168px;height:206px;clip-path:polygon(0 0,100% 0,70% 100%,0 100%);background:linear-gradient(140deg,#d8d2c8,#7c6a57 55%,#b4aa9c)" role="img" aria-label="Team meeting around a wooden table, seen from above"></div>
    <div class="abs" style="left:197px;top:28px;font-size:15px;color:var(--brand)">Your Awesome Text</div>
    <div class="abs" style="left:197px;top:46px;font-size:4.6px;letter-spacing:1.5px;color:var(--grey)">A SHORT SUBTITLE HERE</div>
    <p class="abs tiny" style="left:197px;top:58px;width:165px">Lorem Ipsum is the printing and typesetting industry. Lorem Ipsum has been the standard dummy text ever since the 1500s, when an unknown printer took a galley of type and scrambled it to make a type specimen book. It has survived not only five centuries.</p>
    <div class="card" style="left:113px;top:120px;width:82px;height:80px;background:var(--navy);box-shadow:0 2px 6px rgba(0,0,0,.2)">
      <svg width="18" height="18" viewBox="0 0 20 20" style="margin-top:4px"><circle cx="10" cy="10" r="7" fill="none" stroke="#fff" stroke-width="1.3"/><circle cx="10" cy="10" r="3" fill="none" stroke="#fff" stroke-width="1.3"/></svg>
      <div class="pname" style="color:var(--white)">Project name</div>
      <p class="tiny-w" style="margin-top:3px">Lorem ipsum dolor sit amet, nec an dictas equidem appellantur, ut has commune accommodare.</p>
    </div>
    <div class="card" style="left:200px;top:120px;width:82px;height:80px;background:var(--white);box-shadow:0 1px 5px rgba(0,0,0,.1)">
      <svg width="18" height="18" viewBox="0 0 20 20" style="margin-top:4px"><path d="M4 16 L8 12 M7 13 Q10 4 16 4 Q16 10 7 13 Z" fill="none" stroke="#0356a4" stroke-width="1.3"/></svg>
      <div class="pname">Project name</div>
      <p class="tiny" style="margin-top:3px">Lorem ipsum dolor sit amet, nec an dictas equidem appellantur, ut has commune accommodare.</p>
    </div>
    <div class="card" style="left:287px;top:120px;width:82px;height:80px;background:var(--white);box-shadow:0 1px 5px rgba(0,0,0,.1)">
      <svg width="18" height="18" viewBox="0 0 20 20" style="margin-top:4px"><path d="M4 16 V11 M8 16 V8 M12 16 V10 M16 16 V5" stroke="#0356a4" stroke-width="1.6"/></svg>
      <div class="pname">Project name</div>
      <p class="tiny" style="margin-top:3px">Lorem ipsum dolor sit amet, nec an dictas equidem appellantur, ut has commune accommodare.</p>
    </div>
    <span class="foot-copy">COPYRIGHT © (ALL RIGHTS RESERVED)</span>
    <span class="foot-dash"></span>
    <span class="foot-mark"><i></i>VANTREL</span>
  </article>

  <!-- title + list panel -->
  <article class="slide">
    <div class="abs" style="left:35px;top:42px;font-size:14px;color:var(--brand)">Add Your Title Here</div>
    <div class="abs" style="left:35px;top:59px;font-size:6px;color:var(--grey)">Write here a great subtitle</div>
    <p class="abs tiny" style="left:35px;top:80px;width:135px">Lorem ipsum dolor sit amet, consectetur adipiscing elit, sed do eiusmod tempor incididunt ut labore et dolore magna aliqua. Lorem ipsum dolor sit amet, consectetur adipiscing elit, sed do eiusmod tempor incididunt ut labore et dolore magna aliqua. Ut enim ad minim veniam, quis nostrud exercitation ullamco laboris nisi ut aliquip.</p>
    <p class="abs tiny" style="left:35px;top:128px;width:135px">Lorem ipsum dolor sit amet, consectetur adipiscing elit, sed do eiusmod tempor incididunt ut labore et dolore magna aliqua. Lorem ipsum dolor sit amet, consectetur adipiscing elit, sed do eiusmod tempor incididunt ut labore et dolore magna aliqua.</p>
    <div class="abs" style="left:36px;top:185px;width:65px;height:12px;border-radius:6px;background:var(--navy);color:var(--white);font-size:4.8px;line-height:12px;padding-left:17px">More here...</div>
    <div class="photo" style="left:197px;top:0;width:196px;height:222px;background:linear-gradient(160deg,#1b4a88,#0d3a7b 60%,#1e4d8a)" role="img" aria-label="Business people at work, navy toned"></div>
    <svg class="abs" style="left:226px;top:42px" width="16" height="16" viewBox="0 0 20 20"><rect x="3" y="3" width="14" height="14" rx="2" fill="none" stroke="#fff" stroke-width="1.3"/><path d="M6 8h8M6 12h5" stroke="#fff" stroke-width="1.3"/></svg>
    <div class="abs" style="left:254px;top:32px;width:120px"><div class="pname" style="color:var(--white);font-weight:400">Project name</div><p class="tiny-w" style="margin-top:3px">Lorem Ipsum is simply dummy unknown printer took a galley of type and scrambled it to make.</p></div>
    <svg class="abs" style="left:226px;top:104px" width="16" height="16" viewBox="0 0 20 20"><circle cx="10" cy="10" r="7" fill="none" stroke="#fff" stroke-width="1.3"/><circle cx="10" cy="10" r="3" fill="none" stroke="#fff" stroke-width="1.3"/></svg>
    <div class="abs" style="left:254px;top:94px;width:120px"><div class="pname" style="color:var(--white);font-weight:400">Project name</div><p class="tiny-w" style="margin-top:3px">Lorem Ipsum is simply dummy unknown printer took a galley of type and scrambled it to make.</p></div>
    <svg class="abs" style="left:226px;top:164px" width="16" height="16" viewBox="0 0 20 20"><path d="M4 16 L8 12 M7 13 Q10 4 16 4 Q16 10 7 13 Z" fill="none" stroke="#fff" stroke-width="1.3"/></svg>
    <div class="abs" style="left:254px;top:154px;width:120px"><div class="pname" style="color:var(--white);font-weight:400">Project name</div><p class="tiny-w" style="margin-top:3px">Lorem Ipsum is simply dummy unknown printer took a galley of type and scrambled it to make.</p></div>
    <span class="foot-copy">COPYRIGHT © (ALL RIGHTS RESERVED)</span>
    <span class="foot-dash"></span>
    <span class="foot-mark light"><i></i>VANTREL</span>
  </article>

  <!-- grey header three icons -->
  <article class="slide">
    <div class="abs" style="left:0;top:0;width:393px;height:112px;background:linear-gradient(#4d4e50,#5e5f61)"></div>
    <div class="abs" style="left:0;right:0;top:36px;text-align:center;font-size:15px;color:var(--white)">Add Your Awesome Text Here</div>
    <div class="abs" style="left:0;right:0;top:55px;text-align:center;font-size:6px;color:var(--white)">Your Sub title goes here</div>
    <div class="icon-box lg" style="left:67px;top:88px"><svg viewBox="0 0 20 20"><circle cx="10" cy="10" r="7" fill="none" stroke="#fff" stroke-width="1.3"/><circle cx="10" cy="10" r="3" fill="none" stroke="#fff" stroke-width="1.3"/></svg></div>
    <div class="icon-box lg" style="left:177px;top:88px"><svg viewBox="0 0 20 20"><path d="M4 16 L8 12 M7 13 Q10 4 16 4 Q16 10 7 13 Z" fill="none" stroke="#fff" stroke-width="1.3"/></svg></div>
    <div class="icon-box lg" style="left:287px;top:88px"><svg viewBox="0 0 20 20"><path d="M4 16 V11 M8 16 V8 M12 16 V10 M16 16 V5" stroke="#fff" stroke-width="1.6"/></svg></div>
    <div class="abs" style="left:37px;top:138px;width:100px;text-align:center"><div class="pname">Project name</div><p class="tiny" style="margin-top:4px">Lorem ipsum dolor sit amet, nec an dictas equidem appellantur, ut has commune accommodare. Mea illum, ludus solet idpro.</p></div>
    <div class="abs" style="left:147px;top:138px;width:100px;text-align:center"><div class="pname">Project name</div><p class="tiny" style="margin-top:4px">Lorem ipsum dolor sit amet, nec an dictas equidem appellantur, ut has commune accommodare. Mea illum, ludus solet idpro.</p></div>
    <div class="abs" style="left:257px;top:138px;width:100px;text-align:center"><div class="pname">Project name</div><p class="tiny" style="margin-top:4px">Lorem ipsum dolor sit amet, nec an dictas equidem appellantur, ut has commune accommodare. Mea illum, ludus solet idpro.</p></div>
    <span class="foot-copy">COPYRIGHT © (ALL RIGHTS RESERVED)</span>
    <span class="foot-dash"></span>
    <span class="foot-mark"><i></i>VANTREL</span>
  </article>

  <!-- six icon list -->
  <article class="slide">
    <div class="s-title">Add Your Awesome Text Here</div>
    <div class="s-sub">YOUR SUB TITLE GOES HERE</div>
    <div class="s-rule"></div>
    <div class="icon-box" style="left:46px;top:62px"><svg viewBox="0 0 20 20"><circle cx="10" cy="10" r="7" fill="none" stroke="#fff" stroke-width="1.5"/><circle cx="10" cy="10" r="3" fill="none" stroke="#fff" stroke-width="1.5"/></svg></div>
    <div class="abs" style="left:77px;top:62px;width:110px"><div class="pname">Project name</div><p class="tiny" style="margin-top:2px">Lorem ipsum dolor sit amet, nec an dictas equidem appellantur, ut has commune accommodare. Mea illum, ludus solet idpro.</p></div>
    <div class="icon-box" style="left:216px;top:62px"><svg viewBox="0 0 20 20"><circle cx="10" cy="10" r="7" fill="none" stroke="#fff" stroke-width="1.5"/><circle cx="10" cy="10" r="3" fill="none" stroke="#fff" stroke-width="1.5"/></svg></div>
    <div class="abs" style="left:247px;top:62px;width:110px"><div class="pname">Project name</div><p class="tiny" style="margin-top:2px">Lorem ipsum dolor sit amet, nec an dictas equidem appellantur, ut has commune accommodare. Mea illum, ludus solet idpro.</p></div>
    <div class="icon-box" style="left:46px;top:104px"><svg viewBox="0 0 20 20"><rect x="3" y="4" width="14" height="12" rx="1" fill="none" stroke="#fff" stroke-width="1.5"/></svg></div>
    <div class="abs" style="left:77px;top:104px;width:110px"><div class="pname">Project name</div><p class="tiny" style="margin-top:2px">Lorem ipsum dolor sit amet, nec an dictas equidem appellantur, ut has commune accommodare. Mea illum, ludus solet idpro.</p></div>
    <div class="icon-box" style="left:216px;top:104px"><svg viewBox="0 0 20 20"><rect x="3" y="4" width="14" height="12" rx="1" fill="none" stroke="#fff" stroke-width="1.5"/></svg></div>
    <div class="abs" style="left:247px;top:104px;width:110px"><div class="pname">Project name</div><p class="tiny" style="margin-top:2px">Lorem ipsum dolor sit amet, nec an dictas equidem appellantur, ut has commune accommodare. Mea illum, ludus solet idpro.</p></div>
    <div class="icon-box" style="left:46px;top:146px"><svg viewBox="0 0 20 20"><path d="M10 3 V14 M5 17 H15" stroke="#fff" stroke-width="1.5"/></svg></div>
    <div class="abs" style="left:77px;top:146px;width:110px"><div class="pname">Project name</div><p class="tiny" style="margin-top:2px">Lorem ipsum dolor sit amet, nec an dictas equidem appellantur, ut has commune accommodare. Mea illum, ludus solet idpro.</p></div>
    <div class="icon-box" style="left:216px;top:146px"><svg viewBox="0 0 20 20"><rect x="4" y="3" width="12" height="14" rx="1" fill="none" stroke="#fff" stroke-width="1.5"/><path d="M7 8h6M7 12h6" stroke="#fff" stroke-width="1.5"/></svg></div>
    <div class="abs" style="left:247px;top:146px;width:110px"><div class="pname">Project name</div><p class="tiny" style="margin-top:2px">Lorem ipsum dolor sit amet, nec an dictas equidem appellantur, ut has commune accommodare. Mea illum, ludus solet idpro.</p></div>
    <span class="foot-copy">COPYRIGHT © (ALL RIGHTS RESERVED)</span>
    <span class="foot-dash"></span>
    <span class="foot-mark"><i></i>VANTREL</span>
  </article>

  <!-- nine numbered -->
  <article class="slide">
    <div class="s-title">Add Your Awesome Text Here</div>
    <div class="s-sub">YOUR SUB TITLE GOES HERE</div>
    <div class="s-rule"></div>
    <div class="num-box" style="left:34px;top:67px">01</div><div class="abs" style="left:58px;top:62px;width:85px"><div class="pname">Project name</div><p class="tiny" style="margin-top:2px">Lorem Ipsum is simply dummy unknown printer took a galley of type and scrambled it to make.</p></div>
    <div class="num-box" style="left:155px;top:67px">02</div><div class="abs" style="left:179px;top:62px;width:85px"><div class="pname">Project name</div><p class="tiny" style="margin-top:2px">Lorem Ipsum is simply dummy unknown printer took a galley of type and scrambled it to make.</p></div>
    <div class="num-box" style="left:275px;top:67px">03</div><div class="abs" style="left:299px;top:62px;width:85px"><div class="pname">Project name</div><p class="tiny" style="margin-top:2px">Lorem Ipsum is simply dummy unknown printer took a galley of type and scrambled it to make.</p></div>
    <div class="num-box" style="left:34px;top:114px">04</div><div class="abs" style="left:58px;top:109px;width:85px"><div class="pname">Project name</div><p class="tiny" style="margin-top:2px">Lorem Ipsum is simply dummy unknown printer took a galley of type and scrambled it to make.</p></div>
    <div class="num-box" style="left:155px;top:114px">05</div><div class="abs" style="left:179px;top:109px;width:85px"><div class="pname">Project name</div><p class="tiny" style="margin-top:2px">Lorem Ipsum is simply dummy unknown printer took a galley of type and scrambled it to make.</p></div>
    <div class="num-box" style="left:275px;top:114px">06</div><div class="abs" style="left:299px;top:109px;width:85px"><div class="pname">Project name</div><p class="tiny" style="margin-top:2px">Lorem Ipsum is simply dummy unknown printer took a galley of type and scrambled it to make.</p></div>
    <div class="num-box" style="left:34px;top:160px">07</div><div class="abs" style="left:58px;top:155px;width:85px"><div class="pname">Project name</div><p class="tiny" style="margin-top:2px">Lorem Ipsum is simply dummy unknown printer took a galley of type and scrambled it to make.</p></div>
    <div class="num-box" style="left:155px;top:160px">08</div><div class="abs" style="left:179px;top:155px;width:85px"><div class="pname">Project name</div><p class="tiny" style="margin-top:2px">Lorem Ipsum is simply dummy unknown printer took a galley of type and scrambled it to make.</p></div>
    <div class="num-box" style="left:275px;top:160px">09</div><div class="abs" style="left:299px;top:155px;width:85px"><div class="pname">Project name</div><p class="tiny" style="margin-top:2px">Lorem Ipsum is simply dummy unknown printer took a galley of type and scrambled it to make.</p></div>
    <span class="foot-copy">COPYRIGHT © (ALL RIGHTS RESERVED)</span>
    <span class="foot-dash"></span>
    <span class="foot-mark"><i></i>VANTREL</span>
  </article>

  <!-- table -->
  <article class="slide">
    <div class="s-title">Add Your Awesome Text Here</div>
    <div class="s-sub">YOUR SUB TITLE GOES HERE</div>
    <div class="s-rule"></div>
    <div class="tbl">
      <div class="h">ADD YOUR TITLE</div>
      <div class="h">ADD YOUR TITLE</div>
      <div class="h" style="background:var(--white);color:var(--brand);font-weight:500;font-size:7px;justify-content:center;gap:3px"><i style="width:6px;height:6px;background:var(--brand);display:block"></i>VANTREL</div>
      <div class="h">ADD YOUR TITLE</div>
      <div class="c"><div class="pname">Project name</div><p class="tiny">Lorem Ipsum is simply dummy unknown printer took a galley of type and scrambled it to make.</p></div>
      <div class="c"><div class="pname">Project name</div><p class="tiny">Lorem Ipsum is simply dummy unknown printer took a galley of type and scrambled it to make.</p></div>
      <div class="hl"><div class="pname">Project name</div><p class="tiny-w">Lorem Ipsum is simply dummy unknown printer took a galley of type and scrambled it to make.</p></div>
      <div class="c"><div class="pname">Project name</div><p class="tiny">Lorem Ipsum is simply dummy unknown printer took a galley of type and scrambled it to make.</p></div>
      <div class="c"><div class="pname">Project name</div><p class="tiny">Lorem Ipsum is simply dummy unknown printer took a galley of type and scrambled it to make.</p></div>
      <div class="c"><div class="pname">Project name</div><p class="tiny">Lorem Ipsum is simply dummy unknown printer took a galley of type and scrambled it to make.</p></div>
      <div class="hl"><div class="pname">Project name</div><p class="tiny-w">Lorem Ipsum is simply dummy unknown printer took a galley of type and scrambled it to make.</p></div>
      <div class="c"><div class="pname">Project name</div><p class="tiny">Lorem Ipsum is simply dummy unknown printer took a galley of type and scrambled it to make.</p></div>
    </div>
    <span class="foot-copy">COPYRIGHT © (ALL RIGHTS RESERVED)</span>
    <span class="foot-dash"></span>
    <span class="foot-mark"><i></i>VANTREL</span>
  </article>

  <!-- picture columns -->
  <article class="slide">
    <div class="abs" style="left:0;top:0;width:393px;height:100px;background:var(--navy)"></div>
    <div class="abs" style="left:23px;top:28px;font-size:15px;font-weight:500;color:var(--white)">Text Here</div>
    <div class="abs" style="left:23px;top:47px;font-size:5px;letter-spacing:1.5px;color:var(--white)">SUB TITLE GOES HERE</div>
    <p class="abs tiny-w" style="left:165px;top:24px;width:195px;text-align:justify">Lorem ipsum dolor sit amet, consectetur adipiscing elit, sed do eiusmod tempor incididunt ut labore et dolore magna aliqua. Lorem ipsum dolor sit amet, consectetur adipiscing elit, sed do eiusmod tempor incididunt ut labore et dolore magna aliqua. Ut enim ad minim veniam, quis nostrud exercitation ullamco laboris nisi ut aliquip.</p>
    <div class="abs" style="left:39px;top:73px;width:91px;height:58px;border-radius:4px;background:var(--grey-box);color:var(--white);font-size:5px;font-weight:500;display:flex;align-items:center;justify-content:center">Add Your Picture Here</div>
    <div class="abs" style="left:155px;top:73px;width:91px;height:58px;border-radius:4px;background:var(--grey-box);color:var(--white);font-size:5px;font-weight:500;display:flex;align-items:center;justify-content:center">Add Your Picture Here</div>
    <div class="abs" style="left:271px;top:73px;width:91px;height:58px;border-radius:4px;background:var(--grey-box);color:var(--white);font-size:5px;font-weight:500;display:flex;align-items:center;justify-content:center">Add Your Picture Here</div>
    <div class="abs" style="left:41px;top:146px;width:88px"><div class="pname" style="color:var(--navy);font-size:5px">Your Text Here</div><p class="tiny" style="text-align:justify">Lorem ipsum dolor sit amet, consectetur adipiscing elit, sed do eiusmod tempor incididunt ut labore et dolore magna aliqua.<br>• Lorem ipsum dolor sit amet,<br>• Consectetur adipiscing elit<br>• Sed do eiusmod tempor incididunt<br>• Ut labore et dolore magna aliqua</p></div>
    <div class="abs" style="left:157px;top:146px;width:88px"><div class="pname" style="color:var(--navy);font-size:5px">Your Text Here</div><p class="tiny" style="text-align:justify">Lorem ipsum dolor sit amet, consectetur adipiscing elit, sed do eiusmod tempor incididunt ut labore et dolore magna aliqua.<br>• Lorem ipsum dolor sit amet,<br>• Consectetur adipiscing elit<br>• Sed do eiusmod tempor incididunt<br>• Ut labore et dolore magna aliqua</p></div>
    <div class="abs" style="left:273px;top:146px;width:88px"><div class="pname" style="color:var(--navy);font-size:5px">Your Text Here</div><p class="tiny" style="text-align:justify">Lorem ipsum dolor sit amet, consectetur adipiscing elit, sed do eiusmod tempor incididunt ut labore et dolore magna aliqua.<br>• Lorem ipsum dolor sit amet,<br>• Consectetur adipiscing elit<br>• Sed do eiusmod tempor incididunt<br>• Ut labore et dolore magna aliqua</p></div>
    <span class="foot-copy">COPYRIGHT © (ALL RIGHTS RESERVED)</span>
    <span class="foot-dash"></span>
    <span class="foot-mark"><i></i>VANTREL</span>
  </article>

  <!-- three cards -->
  <article class="slide">
    <div class="s-title">Add Your Awesome Text Here</div>
    <div class="s-sub">YOUR SUB TITLE GOES HERE</div>
    <div class="s-rule"></div>
    <div class="abs" style="left:61px;top:74px;width:84px;height:115px;border:1px solid #e5e5e5;padding:20px 8px 0"><div style="font-size:7.5px;font-weight:500;color:var(--grey-dark);line-height:1.25">Add<br>Awesome<br>Title Here</div><p class="tiny" style="margin-top:5px">Lorem ipsum dolor sit amet, consectetur adipiscing elit, sed do eiusmod tempor incididunt ut labore et dolore magna aliqua.</p></div>
    <div class="abs" style="left:154px;top:74px;width:84px;height:115px;border:1px solid #e5e5e5;padding:20px 8px 0"><div style="font-size:7.5px;font-weight:500;color:var(--grey-dark);line-height:1.25">Add<br>Awesome<br>Title Here</div><p class="tiny" style="margin-top:5px">Lorem ipsum dolor sit amet, consectetur adipiscing elit, sed do eiusmod tempor incididunt ut labore et dolore magna aliqua.</p></div>
    <div class="abs" style="left:246px;top:74px;width:84px;height:115px;border:1px solid #e5e5e5;padding:20px 8px 0"><div style="font-size:7.5px;font-weight:500;color:var(--grey-dark);line-height:1.25">Add<br>Awesome<br>Title Here</div><p class="tiny" style="margin-top:5px">Lorem ipsum dolor sit amet, consectetur adipiscing elit, sed do eiusmod tempor incididunt ut labore et dolore magna aliqua.</p></div>
    <div class="icon-box" style="left:90px;top:58px"><svg viewBox="0 0 20 20"><circle cx="10" cy="10" r="7" fill="none" stroke="#fff" stroke-width="1.5"/><circle cx="10" cy="10" r="3" fill="none" stroke="#fff" stroke-width="1.5"/></svg></div>
    <div class="icon-box" style="left:183px;top:58px"><svg viewBox="0 0 20 20"><rect x="3" y="4" width="14" height="12" rx="1" fill="none" stroke="#fff" stroke-width="1.5"/></svg></div>
    <div class="icon-box" style="left:276px;top:58px"><svg viewBox="0 0 20 20"><path d="M10 3 V14 M5 17 H15" stroke="#fff" stroke-width="1.5"/></svg></div>
    <span class="foot-copy">COPYRIGHT © (ALL RIGHTS RESERVED)</span>
    <span class="foot-dash"></span>
    <span class="foot-mark"><i></i>VANTREL</span>
  </article>

  <!-- timeline -->
  <article class="slide">
    <div class="s-title">Add Your Awesome Text Here</div>
    <div class="s-sub">YOUR SUB TITLE GOES HERE</div>
    <div class="s-rule"></div>
    <svg class="abs" style="left:0;top:0" width="393" height="222"><path d="M28 46 Q22 64 58 64 H340 A31 31 0 0 1 340 127 H40 Q10 127 22 160 L60 210" fill="none" stroke="#d5d9de" stroke-width="1"/></svg>
    <div class="year-dot" style="left:77px;top:61px"></div><div class="year" style="left:76px;top:72px">2015</div><p class="abs tiny" style="left:81px;top:82px;width:60px">Lorem Ipsum is simply dummy unknown printer took a galley of type and scrambled it to make.</p>
    <div class="year-dot" style="left:168px;top:61px"></div><div class="year" style="left:167px;top:72px">2016</div><p class="abs tiny" style="left:172px;top:82px;width:60px">Lorem Ipsum is simply dummy unknown printer took a galley of type and scrambled it to make.</p>
    <div class="year-dot" style="left:260px;top:61px"></div><div class="year" style="left:259px;top:72px">2017</div><p class="abs tiny" style="left:264px;top:82px;width:60px">Lorem Ipsum is simply dummy unknown printer took a galley of type and scrambled it to make.</p>
    <div class="year-dot" style="left:77px;top:124px"></div><div class="year" style="left:76px;top:135px">2018</div><p class="abs tiny" style="left:81px;top:145px;width:60px">Lorem Ipsum is simply dummy unknown printer took a galley of type and scrambled it to make.</p>
    <div class="year-dot" style="left:168px;top:124px"></div><div class="year" style="left:167px;top:135px">2019</div><p class="abs tiny" style="left:172px;top:145px;width:60px">Lorem Ipsum is simply dummy unknown printer took a galley of type and scrambled it to make.</p>
    <div class="year-dot" style="left:260px;top:124px"></div><div class="year" style="left:259px;top:135px">2020</div><p class="abs tiny" style="left:264px;top:145px;width:60px">Lorem Ipsum is simply dummy unknown printer took a galley of type and scrambled it to make.</p>
    <span class="foot-copy">COPYRIGHT © (ALL RIGHTS RESERVED)</span>
    <span class="foot-dash"></span>
    <span class="foot-mark"><i></i>VANTREL</span>
  </article>

  <!-- comparison -->
  <article class="slide">
    <div class="s-title">Comparison Slide</div>
    <div class="s-sub">YOUR SUB TITLE GOES HERE</div>
    <div class="s-rule"></div>
    <div class="abs" style="left:26px;top:86px;width:95px"><div class="pname" style="color:var(--navy)">Lorem ipsum dolor</div><p class="tiny" style="margin-top:3px">Lorem ipsum dolor sit amet, consectetur adipiscing elit, sed do eiusmod tempor</p><p class="tiny" style="margin-top:6px;line-height:1.9">▸ Lorem ipsum dolor<br>▸ Sit amet consectetur adipiscing<br>▸ Do eiusmod tempor<br>▸ El pero ipsun do<br>▸ Lorem ipsum dolor</p></div>
    <div class="abs" style="left:283px;top:86px;width:95px"><div class="pname" style="color:var(--navy)">Lorem ipsum dolor</div><p class="tiny" style="margin-top:3px">Lorem ipsum dolor sit amet, consectetur adipiscing elit, sed do eiusmod tempor</p><p class="tiny" style="margin-top:6px;line-height:1.9">▸ Lorem ipsum dolor<br>▸ Sit amet consectetur adipiscing<br>▸ Do eiusmod tempor<br>▸ El pero ipsun do<br>▸ Lorem ipsum dolor</p></div>
    <svg class="abs" style="left:115px;top:90px" width="165" height="70" viewBox="0 0 165 70">
      <path d="M2 21 L22 1 H60 V11 H35 Z" fill="#58595b"/><path d="M2 21 H70 V31 H2 Z" fill="#58595b"/>
      <path d="M2 49 L22 69 H60 V59 H35 Z" fill="#58595b"/><path d="M2 39 H70 V49 H2 Z" fill="#58595b"/>
      <path d="M163 21 L143 1 H105 V11 H130 Z" fill="#0b3a7c"/><path d="M163 21 H95 V31 H163 Z" fill="#0b3a7c"/>
      <path d="M163 49 L143 69 H105 V59 H130 Z" fill="#0b3a7c"/><path d="M163 39 H95 V49 H163 Z" fill="#0b3a7c"/>
      <circle cx="82.5" cy="35" r="31" fill="#fff"/>
      <rect x="72" y="25" width="20" height="20" fill="none" stroke="#0356a4" stroke-width="1.6"/>
    </svg>
    <span class="foot-copy">COPYRIGHT © (ALL RIGHTS RESERVED)</span>
    <span class="foot-dash"></span>
    <span class="foot-mark"><i></i>VANTREL</span>
  </article>

  <!-- six segment cycle -->
  <article class="slide">
    <div class="s-title">Add Your Awesome Text Here</div>
    <div class="s-sub">YOUR SUB TITLE GOES HERE</div>
    <div class="s-rule"></div>
    <svg class="abs" style="left:131px;top:64px" width="130" height="130" viewBox="0 0 130 130">
      <g fill="none" stroke-width="30" transform="rotate(-90 65 65)">
        <circle cx="65" cy="65" r="46" stroke="#0356a4" stroke-dasharray="45 244" transform="rotate(1 65 65)"/>
        <circle cx="65" cy="65" r="46" stroke="#0b3a7c" stroke-dasharray="45 244" transform="rotate(61 65 65)"/>
        <circle cx="65" cy="65" r="46" stroke="#58595b" stroke-dasharray="45 244" transform="rotate(121 65 65)"/>
        <circle cx="65" cy="65" r="46" stroke="#0356a4" stroke-dasharray="45 244" transform="rotate(181 65 65)"/>
        <circle cx="65" cy="65" r="46" stroke="#0b3a7c" stroke-dasharray="45 244" transform="rotate(241 65 65)"/>
        <circle cx="65" cy="65" r="46" stroke="#58595b" stroke-dasharray="45 244" transform="rotate(301 65 65)"/>
      </g>
      <circle cx="65" cy="65" r="26" fill="#fff" stroke="#d8d8d8"/>
      <rect x="56" y="56" width="18" height="18" fill="none" stroke="#0356a4" stroke-width="1.5"/>
    </svg>
    <div class="abs" style="left:52px;top:64px;width:85px;text-align:right"><div class="pname" style="color:var(--navy)">Lorem ipsum dolor</div><p class="tiny">Lorem ipsum dolor sit amet, consectetur adipiscing elit, sed do eiusmod tempor</p></div>
    <div class="abs" style="left:36px;top:117px;width:85px;text-align:right"><div class="pname" style="color:var(--navy)">Lorem ipsum dolor</div><p class="tiny">Lorem ipsum dolor sit amet, consectetur adipiscing elit, sed do eiusmod tempor</p></div>
    <div class="abs" style="left:55px;top:173px;width:85px;text-align:right"><div class="pname" style="color:var(--navy)">Lorem ipsum dolor</div><p class="tiny">Lorem ipsum dolor sit amet, consectetur adipiscing elit, sed do eiusmod tempor</p></div>
    <div class="abs" style="left:253px;top:63px;width:85px"><div class="pname" style="color:var(--navy)">Lorem ipsum dolor</div><p class="tiny">Lorem ipsum dolor sit amet, consectetur adipiscing elit, sed do eiusmod tempor</p></div>
    <div class="abs" style="left:276px;top:118px;width:85px"><div class="pname" style="color:var(--navy)">Lorem ipsum dolor</div><p class="tiny">Lorem ipsum dolor sit amet, consectetur adipiscing elit, sed do eiusmod tempor</p></div>
    <div class="abs" style="left:255px;top:172px;width:85px"><div class="pname" style="color:var(--navy)">Lorem ipsum dolor</div><p class="tiny">Lorem ipsum dolor sit amet, consectetur adipiscing elit, sed do eiusmod tempor</p></div>
    <span class="foot-copy">COPYRIGHT © (ALL RIGHTS RESERVED)</span>
    <span class="foot-dash"></span>
    <span class="foot-mark"><i></i>VANTREL</span>
  </article>

  <!-- three part donut -->
  <article class="slide">
    <svg class="abs" style="left:30px;top:44px" width="140" height="140" viewBox="0 0 140 140">
      <g fill="none" stroke-width="44">
        <circle cx="70" cy="70" r="44" stroke="#4d4e50" stroke-dasharray="88 188" transform="rotate(152 70 70)"/>
        <circle cx="70" cy="70" r="44" stroke="#0b3a7c" stroke-dasharray="88 188" transform="rotate(272 70 70)"/>
        <circle cx="70" cy="70" r="44" stroke="#0356a4" stroke-dasharray="88 188" transform="rotate(32 70 70)"/>
      </g>
      <text x="70" y="118" text-anchor="middle" font-family="Rubik,sans-serif" font-size="5" fill="#fff">Add Your Title Here</text>
      <text x="36" y="60" text-anchor="middle" font-family="Rubik,sans-serif" font-size="5" fill="#fff" transform="rotate(-60 36 60)">Add Your Title Here</text>
      <text x="104" y="60" text-anchor="middle" font-family="Rubik,sans-serif" font-size="5" fill="#fff" transform="rotate(60 104 60)">Add Your Title Here</text>
    </svg>
    <div class="abs" style="left:213px;top:36px;font-size:14px;color:var(--brand)">Add Your Title Here</div>
    <div class="abs" style="left:213px;top:52px;font-size:6px;color:var(--grey)">Write here a great subtitle</div>
    <div class="icon-box" style="left:213px;top:82px"><svg viewBox="0 0 20 20"><circle cx="10" cy="10" r="7" fill="none" stroke="#fff" stroke-width="1.5"/><circle cx="10" cy="10" r="3" fill="none" stroke="#fff" stroke-width="1.5"/></svg></div>
    <div class="abs" style="left:243px;top:78px;width:100px"><div class="pname">Project name</div><p class="tiny" style="margin-top:2px">Lorem ipsum dolor sit amet, nec an dictas equidem appellantur, ut has commune accommodare. Mea illum, ludus solet idpro</p></div>
    <div class="icon-box" style="left:213px;top:123px;background:var(--brand)"><svg viewBox="0 0 20 20"><rect x="3" y="6" width="10" height="8" fill="none" stroke="#fff" stroke-width="1.5"/><path d="M13 9 H17 V14 H13" fill="none" stroke="#fff" stroke-width="1.5"/></svg></div>
    <div class="abs" style="left:243px;top:119px;width:100px"><div class="pname">Project name</div><p class="tiny" style="margin-top:2px">Lorem ipsum dolor sit amet, nec an dictas equidem appellantur, ut has commune accommodare. Mea illum, ludus solet idpro</p></div>
    <div class="icon-box" style="left:213px;top:164px;background:var(--grey-dark)"><svg viewBox="0 0 20 20"><rect x="3" y="4" width="14" height="13" rx="1" fill="none" stroke="#fff" stroke-width="1.5"/><path d="M3 8 H17" stroke="#fff" stroke-width="1.5"/></svg></div>
    <div class="abs" style="left:243px;top:160px;width:100px"><div class="pname">Project name</div><p class="tiny" style="margin-top:2px">Lorem ipsum dolor sit amet, nec an dictas equidem appellantur, ut has commune accommodare. Mea illum, ludus solet idpro</p></div>
    <span class="foot-copy">COPYRIGHT © (ALL RIGHTS RESERVED)</span>
    <span class="foot-dash"></span>
    <span class="foot-mark"><i></i>VANTREL</span>
  </article>

  <!-- four step loop -->
  <article class="slide">
    <div class="s-title">Add Your Awesome Text Here</div>
    <div class="s-sub">YOUR SUB TITLE GOES HERE</div>
    <div class="s-rule"></div>
    <svg class="abs" style="left:148px;top:62px" width="100" height="112" viewBox="0 0 100 112">
      <path d="M14 26 V12 H70 V4 L86 18 L70 32 V24 H26 V26 Z" fill="#4d4e50"/>
      <path d="M74 22 H88 V80 H96 L82 96 L68 80 H76 V22 Z" fill="#4d4e50"/>
      <path d="M86 86 V100 H30 V108 L14 94 L30 80 V88 H74 V86 Z" fill="#4d4e50"/>
      <path d="M26 90 H12 V32 H4 L18 16 L32 32 H24 V90 Z" fill="#0b3a7c"/>
      <text x="50" y="20" text-anchor="middle" font-family="Rubik,sans-serif" font-size="4.5" fill="#fff">Your Text Here</text>
      <text x="50" y="97" text-anchor="middle" font-family="Rubik,sans-serif" font-size="4.5" fill="#fff">Your Text Here</text>
      <text x="20" y="62" text-anchor="middle" font-family="Rubik,sans-serif" font-size="4.5" fill="#fff" transform="rotate(-90 20 62)">Your Text Here</text>
      <text x="82" y="52" text-anchor="middle" font-family="Rubik,sans-serif" font-size="4.5" fill="#fff" transform="rotate(90 82 52)">Your Text Here</text>
    </svg>
    <div class="abs" style="left:55px;top:66px;width:80px;text-align:right"><div style="font-size:6px;font-weight:500;color:var(--grey-dark)">Step 01</div><p class="tiny">Lorem ipsom dolor consectetur dolor</p></div>
    <div class="abs" style="left:262px;top:66px;width:80px"><div style="font-size:6px;font-weight:500;color:var(--grey-dark)">Step 01</div><p class="tiny">Lorem ipsom dolor consectetur dolor</p></div>
    <div class="abs" style="left:55px;top:157px;width:80px;text-align:right"><div style="font-size:6px;font-weight:500;color:var(--grey-dark)">Step 03</div><p class="tiny">Lorem ipsom dolor consectetur dolor</p></div>
    <div class="abs" style="left:262px;top:157px;width:80px"><div style="font-size:6px;font-weight:500;color:var(--grey-dark)">Step 04</div><p class="tiny">Lorem ipsom dolor consectetur dolor</p></div>
    <span class="foot-copy">COPYRIGHT © (ALL RIGHTS RESERVED)</span>
    <span class="foot-dash"></span>
    <span class="foot-mark"><i></i>VANTREL</span>
  </article>

  <!-- contact -->
  <article class="slide" style="background:linear-gradient(135deg,#ffffff,#f2f5f8 60%,#ffffff)">
    <div class="pill on" style="top:50px"><svg viewBox="0 0 10 10"><circle cx="5" cy="5" r="4" fill="none" stroke="#fff"/><path d="M1 5 H9 M5 1 Q2 5 5 9 Q8 5 5 1" fill="none" stroke="#fff" stroke-width=".7"/></svg>www.example-site.com</div>
    <div class="pill" style="top:79px;height:21px;line-height:1.3"><svg viewBox="0 0 10 10"><path d="M5 9 Q1 5 1 3.5 A4 3.5 0 0 1 9 3.5 Q9 5 5 9 Z" fill="none" stroke="#0b3a7c"/></svg><span>Here to write your<br>Company adress</span></div>
    <div class="pill" style="top:108px"><svg viewBox="0 0 10 10"><path d="M2 1 L4 1 L4.8 3.4 L3.6 4.2 Q4.6 6 5.8 6.5 L6.6 5.3 L9 6 V8 Q5 9 1.5 4 Q1 2 2 1 Z" fill="#0b3a7c"/></svg>(555) 014-0505</div>
    <div class="pill" style="top:137px"><svg viewBox="0 0 10 10"><rect x="1" y="2" width="8" height="6" fill="#0b3a7c"/><path d="M1 2 L5 5.5 L9 2" fill="none" stroke="#fff" stroke-width=".8"/></svg>info@example-site.com</div>
    <div class="abs" style="left:82px;top:178px;display:flex;gap:4px"><i style="width:7px;height:7px;background:var(--grey-dark);display:block"></i><i style="width:7px;height:7px;background:var(--grey-dark);display:block"></i><i style="width:7px;height:7px;background:var(--grey-dark);display:block"></i><i style="width:7px;height:7px;background:var(--grey-dark);display:block"></i></div>
    <div class="abs" style="left:215px;top:98px;display:flex;align-items:center;gap:5px;font-size:15px;font-weight:500;color:var(--brand)"><i style="width:16px;height:16px;background:var(--brand);display:block"></i>VANTREL</div>
  </article>

</main>
</body>
</html>
```